Electrician Business Card/ company logo/small business

New Business Cards and logo needed that will catch peoples eye and say we went that extra step. Attached is a design possibly to be incorporated, if u have your own great, lets see it!... This will be a small local business. thank you for all you do!
Corvane Electric
Wren Osloby Owner
Journeyman Electrician
phone 1.360.428.6037
email: KLXCorvaneElectric@mailvex.net
call for free estimate!

Target Market(s)

support small local business

Industry/Entity Type

Electrical,

Contact Information for Business Card

name, title,company/ logo, phone, email, free estimate

Font styles to use
Other font styles liked:
• easy to read

Colors

Designer to choose colors to be used in the design.

Requirements
Must have
• eye catching everything! logo and corvane electric listed on business card/logo, incorp logo in the background of card
Nice to have
• lightening bolts in eyes or around the triangle? vertical, modern, any design that would be unique and stand out
Should not have
• pinks, reds, yellows,brown

```html
<!DOCTYPE html>
<html lang="en">
<head>
<meta charset="utf-8">
<title>Corvane Electric – Business Card</title>
<link href="https://fonts.googleapis.com/css2?family=Overpass:wght@400;600;700;800&display=swap" rel="stylesheet">
<style>
  :root {
    --navy: #00315f;
    --royal: #0254ab;
    --royal-band: #0e5fb4;
    --white: #ffffff;
    --pale-band: #e8eff7;
    --ink: #0a0a0a;
  }
  * { margin: 0; padding: 0; box-sizing: border-box; }
  html, body { width: 1200px; height: 1200px; overflow: hidden; }
  body {
    background: var(--navy);
    font-family: "Overpass", sans-serif;
    position: relative;
  }
  .card {
    position: absolute;
    left: 324px;
    width: 552px;
    height: 346px;
    overflow: hidden;
    box-shadow: 0 18px 50px rgba(0, 20, 50, 0.45);
  }
  .card-bands { position: absolute; inset: 0; width: 100%; height: 100%; }
  .card--front { top: 206px; background: var(--royal); }
  .card--back  { top: 647px; background: var(--white); }

  .brand-disc {
    position: absolute;
    left: 238px; top: 68px;
    width: 76px; height: 76px;
    border-radius: 50%;
    background: var(--white);
  }
  .front-wordmark {
    position: absolute;
    left: 0; right: 0; top: 238px;
    text-align: center;
    color: var(--white);
    font-weight: 700;
    font-size: 35px;
    letter-spacing: 0.5px;
    line-height: 1;
  }

  .person-name {
    position: absolute;
    left: 59px; top: 72px;
    font-weight: 700;
    font-size: 25px;
    color: var(--ink);
    letter-spacing: 0.6px;
    line-height: 1;
  }
  .person-title {
    position: absolute;
    left: 59px; top: 111px;
    font-weight: 400;
    font-size: 15px;
    color: var(--royal);
    letter-spacing: 0.3px;
    line-height: 1;
  }
  .back-brand {
    position: absolute;
    left: 340px; top: 80px;
    width: 196px;
    display: flex; align-items: center; justify-content: center; gap: 7px;
    font-weight: 700;
    font-size: 17px;
    color: var(--royal);
    line-height: 1;
  }
  .back-brand-mark { width: 9px; height: 9px; background: var(--royal); flex: none; }

  .contact-list { list-style: none; position: absolute; left: 38px; top: 217px; }
  .contact-item {
    display: flex; align-items: center;
    height: 22px;
    margin-bottom: 16px;
    font-size: 17px;
    color: var(--ink);
    line-height: 1;
  }
  .contact-item::before {
    content: "";
    width: 6px; height: 6px;
    background: var(--royal);
    margin-right: 14px;
    flex: none;
  }
</style>
</head>
<body>

  <section class="card card--front" aria-label="Card front">
    <svg class="card-bands" viewBox="0 0 890 558" preserveAspectRatio="none" aria-hidden="true">
      <polygon fill="var(--royal-band)" points="79,0 127,0 445,394 764,0 811,0 445,452"/>
      <polygon fill="var(--royal-band)" points="0,81 0,182 307,558 386,558"/>
      <polygon fill="var(--royal-band)" points="890,81 890,182 584,558 505,558"/>
    </svg>
    <div class="brand-disc" aria-hidden="true"></div>
    <h1 class="front-wordmark">Corvane Electric</h1>
  </section>

  <section class="card card--back" aria-label="Card back">
    <svg class="card-bands" viewBox="0 0 890 558" preserveAspectRatio="none" aria-hidden="true">
      <polygon fill="var(--pale-band)" points="890,36 890,195 595,558 468,558"/>
      <polygon fill="var(--pale-band)" points="0,404 0,558 127,558"/>
    </svg>
    <h2 class="person-name">Wren Osloby</h2>
    <p class="person-title">Journeyman Electrician</p>
    <div class="back-brand"><span class="back-brand-mark"></span>Corvane Electric</div>
    <ul class="contact-list">
      <li class="contact-item">1.360.428.6037</li>
      <li class="contact-item">KLXCorvaneElectric@mailvex.net</li>
    </ul>
  </section>

</body>
</html>
```